Consulting Group Needs a Graphic Design

We have created a unique, cyclical process to describe our company's philosophy on parenting to our clients. It is provided in the attached file. At the center of the graphic design, which includes all written words on the page, is an image of a gardener that we really like. We found it through a clipart service, but we are not able to trademark it as our own. We would like to create a similar image which includes the female gardener tending the garden, with a trowel in her hand and a watering can at her side. We want the flowers in her garden to be different, just as every child is unique and different within the same family. For more perspective on our company, please visit www.brookvaleguidance.com.
Updates

Project Deadline Extended
Reason: Some of the designers are getting very close to what we want. Due to some unforeseen circumstances, we were unable to give feedback for a couple of days. We would really appreciate your consideration of our request. We are eager to get the design finished to move forward with our branding strategy, so we will be hyper-focused on the project over the coming days. Thank you, Brookvale Family Advisors

Project Deadline Extended
Reason: We would like to give our first choice designer a chance to create a complementary logo to accompany his submission. We have been in communication with this designer.

Industry/Entity Type

Gardener

```html
<!DOCTYPE html>
<html lang="en">
<head>
<meta charset="utf-8">
<title>The Brookvale Parenting Method</title>
<link href="https://fonts.googleapis.com/css2?family=Jost:wght@500;600&display=swap" rel="stylesheet">
<style>
  :root {
    --paper: #ffffff;
    --forest: #0d6b3a;
    --field: #0f9a47;
    --ring: #177a3a;
    --leaf: #7ccb4c;
    --bark: #6b3a12;
    --tone-blue: #1aa6df;
    --tone-brown: #6b3a12;
    --tone-orange: #f5921e;
  }
  html, body {
    margin: 0;
    padding: 0;
    width: 1200px;
    height: 970px;
    overflow: hidden;
    background: var(--paper);
  }
  .method-diagram {
    display: block;
    width: 1200px;
    height: 970px;
  }
  .method-title {
    font-family: "Jost", sans-serif;
    font-weight: 600;
    font-size: 34px;
    fill: var(--forest);
  }
  .method-title .tm { font-size: 11px; }
  .cycle-field { fill: var(--field); }
  .cycle-arrow {
    fill: none;
    stroke: var(--ring);
    stroke-width: 8;
  }
  .arrow-head { fill: var(--ring); }
  .step-badge { fill: var(--leaf); stroke: var(--field); stroke-width: 2; }
  .step-label {
    font-family: "Jost", sans-serif;
    font-weight: 500;
    font-size: 15px;
    fill: var(--bark);
    text-anchor: middle;
  }
  .copyright {
    font-family: "Jost", sans-serif;
    font-weight: 500;
    font-size: 13px;
    fill: var(--forest);
    text-anchor: middle;
  }
</style>
</head>
<body>
<svg class="method-diagram" viewBox="0 0 712 576" xmlns="http://www.w3.org/2000/svg">
  <defs>
    <marker id="arrowhead" viewBox="0 0 10 10" refX="4" refY="5" markerUnits="userSpaceOnUse" markerWidth="22" markerHeight="22" orient="auto">
      <path class="arrow-head" d="M0,0 L10,5 L0,10 Z"/>
    </marker>
    <linearGradient id="gardenTone" x1="0" y1="0" x2="1" y2="1">
      <stop offset="0%" stop-color="var(--tone-brown)" stop-opacity="0.55"/>
      <stop offset="40%" stop-color="var(--tone-blue)" stop-opacity="0.55"/>
      <stop offset="100%" stop-color="var(--tone-orange)" stop-opacity="0.55"/>
    </linearGradient>
  </defs>

  <text class="method-title" x="356" y="92" text-anchor="middle">The Brookvale Parenting Method<tspan class="tm" dy="-18">™</tspan></text>

  <ellipse class="cycle-field" cx="358" cy="327" rx="288" ry="198"/>

  <g class="cycle-arrows">
    <path class="cycle-arrow" d="M127,217 A282,192 0 0 1 280,143" marker-end="url(#arrowhead)"/>
    <path class="cycle-arrow" d="M431,142 A282,192 0 0 1 566,198" marker-end="url(#arrowhead)"/>
    <path class="cycle-arrow" d="M639,310 A282,192 0 0 1 596,430" marker-end="url(#arrowhead)"/>
    <path class="cycle-arrow" d="M431,512 A282,192 0 0 1 295,514" marker-end="url(#arrowhead)"/>
    <path class="cycle-arrow" d="M142,450 A282,192 0 0 1 77,336" marker-end="url(#arrowhead)"/>
  </g>

  <rect class="garden-scene" role="img" aria-label="Illustration of a kneeling woman gardener with a trowel and a watering can, tending a row of different flowers" x="210" y="175" width="335" height="255" rx="20" fill="url(#gardenTone)"/>

  <g class="cycle-steps">
    <g class="step" transform="translate(358,140)">
      <ellipse class="step-badge" rx="62" ry="30"/>
      <text class="step-label"><tspan x="0" y="-3">Plant with</tspan><tspan x="0" y="15">purpose</tspan></text>
    </g>
    <g class="step" transform="translate(612,245) rotate(62)">
      <ellipse class="step-badge" rx="52" ry="30"/>
      <text class="step-label" y="5">Nurture</text>
    </g>
    <g class="step" transform="translate(502,475) rotate(-40)">
      <ellipse class="step-badge" rx="58" ry="30"/>
      <text class="step-label"><tspan x="0" y="-3">Enrich</tspan><tspan x="0" y="15">the soil</tspan></text>
    </g>
    <g class="step" transform="translate(205,475) rotate(18)">
      <ellipse class="step-badge" rx="60" ry="30"/>
      <text class="step-label"><tspan x="0" y="-3">Prune as</tspan><tspan x="0" y="15">needed</tspan></text>
    </g>
    <g class="step" transform="translate(98,250) rotate(-66)">
      <ellipse class="step-badge" rx="58" ry="30"/>
      <text class="step-label"><tspan x="0" y="-3">Measure</tspan><tspan x="0" y="15">progress</tspan></text>
    </g>
  </g>

  <text class="copyright" x="358" y="545">© Brookvale Family Advisors</text>
</svg>
</body>
</html>
```